Craft brewery keg badge / badge branding to be on display on keg fonts in pubs and craft beer bars

We're a small craft beer producer and are looking to have a keg badge designed to be put onto keg fonts in bars as well as being used on our bottles. Our website is www.qelmarbrewing.co.uk. -Please take a look at our site however we're looking for new branding! We're not looking to have the windmill on the badge! We want a bold geometric hop design in the centre of the design. The beer is a low AVB beer (2.9% ABV) and will be hopped with Cascade, Colombus and Mosaic hops and will have a fruity / juicy aroma. We're looking to have a design that we can re-use again and again by changing: colours and wording for different beers in the future.

Target Market(s)
Craft beer drinkers
Industry/Entity Type
Craft Brewery
Requirements
Must have
- Simple, elegant, repeatable core message from the badge. It need a simple, bold geometric hop design (examples uploaded) in the centre which is repeatable across many brands in the future.
- The badge needs to be circular and 82mm across to fit our tap lenses (see http://www.drevix.co.uk/branding for the flat lens). The keg badge needs to be modern and in line with other keg badges like the examples attached- though we leave the artistic flair up to you guys. Please see below the styles of keg badge we like.
- Must be in vector file format and we must get a jpeg version too.

Should not have
- Should not be overcrowded and try to be too full of information. See attached examples.

```html
<!DOCTYPE html>
<html lang="en">
<head>
<meta charset="utf-8">
<title>Keg Badge Colourways</title>
<link rel="stylesheet" href="https://fonts.googleapis.com/css2?family=Exo+2:wght@600;800&display=swap">
<style>
  :root {
    --canvas: #fefcb6;
    --ink: #ffffff;
    --hop-light: #f7f05a;
    --hop-mid: #f1d444;
    --hop-dark: #f2b040;
    --olive-a: #8f8a40;
    --olive-m: #6f7422;
    --olive-b: #4a5214;
    --amber-a: #966250;
    --amber-m: #7a4a26;
    --amber-b: #4c2a10;
    --ruby-a: #904252;
    --ruby-m: #72202a;
    --ruby-b: #45100f;
    --slate-a: #7c7c7c;
    --slate-m: #555555;
    --slate-b: #2e2e2e;
    --ocean-a: #43819c;
    --ocean-m: #24557c;
    --ocean-b: #0f2a50;
  }
  * { margin: 0; padding: 0; box-sizing: border-box; }
  html, body { width: 1200px; height: 806px; overflow: hidden; background: var(--canvas); }
  .sheet { position: relative; width: 1200px; height: 806px; font-family: "Exo 2", sans-serif; color: var(--ink); }

  .badge {
    position: absolute;
    width: 349px; height: 349px;
    border-radius: 50%;
    overflow: hidden;
    text-align: center;
  }
  .badge--olive { left: 35px;  top: 46px; }
  .badge--amber { left: 418px; top: 47px; }
  .badge--ruby  { left: 798px; top: 46px; }
  .badge--slate { left: 228px; top: 412px; }
  .badge--ocean { left: 610px; top: 416px; }

  .badge__field { position: absolute; inset: 0; }
  .badge--olive .badge__field { background: linear-gradient(165deg, var(--olive-a) 0%, var(--olive-m) 55%, var(--olive-b) 100%); }
  .badge--amber .badge__field { background: linear-gradient(165deg, var(--amber-a) 0%, var(--amber-m) 55%, var(--amber-b) 100%); }
  .badge--ruby  .badge__field { background: linear-gradient(165deg, var(--ruby-a) 0%, var(--ruby-m) 55%, var(--ruby-b) 100%); }
  .badge--slate .badge__field { background: linear-gradient(165deg, var(--slate-a) 0%, var(--slate-m) 55%, var(--slate-b) 100%); }
  .badge--ocean .badge__field { background: linear-gradient(165deg, var(--ocean-a) 0%, var(--ocean-m) 55%, var(--ocean-b) 100%); }

  .badge__hop {
    position: absolute;
    left: 99px; top: 32px;
    width: 150px; height: 206px;
    border-radius: 45% 45% 50% 50% / 25% 25% 75% 75%;
    background: linear-gradient(180deg, var(--hop-light) 0%, var(--hop-mid) 50%, var(--hop-dark) 100%);
  }
  .badge__name {
    position: absolute;
    left: 0; right: 0; top: 260px;
    font-weight: 800;
    font-size: 22px;
    line-height: 1;
  }
  .badge__rule {
    position: absolute;
    left: 74px; width: 201px; top: 283px;
    height: 2px; background: var(--ink);
  }
  .badge__brewer {
    position: absolute;
    left: 0; right: 0; top: 288px;
    font-weight: 600;
    font-size: 10.5px;
    line-height: 12px;
    letter-spacing: 0.2px;
  }
  .badge__abv {
    position: absolute;
    left: 0; right: 0; top: 312px;
    font-weight: 600;
    font-size: 10.5px;
    line-height: 12px;
  }
</style>
</head>
<body>
<main class="sheet">
  <section class="badge badge--olive">
    <div class="badge__field" role="img" aria-label="Faceted geometric background in olive tones"></div>
    <div class="badge__hop" role="img" aria-label="Bold geometric hop cone illustration"></div>
    <div class="badge__name">BRAND NAME</div>
    <div class="badge__rule"></div>
    <div class="badge__brewer">QELMAR BREWING CO. LTD</div>
    <div class="badge__abv">2.9% ABV</div>
  </section>
  <section class="badge badge--amber">
    <div class="badge__field" role="img" aria-label="Faceted geometric background in amber tones"></div>
    <div class="badge__hop" role="img" aria-label="Bold geometric hop cone illustration"></div>
    <div class="badge__name">BRAND NAME</div>
    <div class="badge__rule"></div>
    <div class="badge__brewer">QELMAR BREWING CO. LTD</div>
    <div class="badge__abv">2.9% ABV</div>
  </section>
  <section class="badge badge--ruby">
    <div class="badge__field" role="img" aria-label="Faceted geometric background in ruby tones"></div>
    <div class="badge__hop" role="img" aria-label="Bold geometric hop cone illustration"></div>
    <div class="badge__name">BRAND NAME</div>
    <div class="badge__rule"></div>
    <div class="badge__brewer">QELMAR BREWING CO. LTD</div>
    <div class="badge__abv">2.9% ABV</div>
  </section>
  <section class="badge badge--slate">
    <div class="badge__field" role="img" aria-label="Faceted geometric background in slate grey tones"></div>
    <div class="badge__hop" role="img" aria-label="Bold geometric hop cone illustration"></div>
    <div class="badge__name">BRAND NAME</div>
    <div class="badge__rule"></div>
    <div class="badge__brewer">QELMAR BREWING CO. LTD</div>
    <div class="badge__abv">2.9% ABV</div>
  </section>
  <section class="badge badge--ocean">
    <div class="badge__field" role="img" aria-label="Faceted geometric background in ocean blue tones"></div>
    <div class="badge__hop" role="img" aria-label="Bold geometric hop cone illustration"></div>
    <div class="badge__name">BRAND NAME</div>
    <div class="badge__rule"></div>
    <div class="badge__brewer">QELMAR BREWING CO. LTD</div>
    <div class="badge__abv">2.9% ABV</div>
  </section>
</main>
</body>
</html>
```